Wine Label for a Prosecco Wine Called Vuro

Prosecco is a white sparkling wine from Italy. We are looking for an eye catching, elegant label for this prosecco that is called "Vuro" because it is a young, fresh, lively white sparkling wine. (We do not want to see children or babies featured on the label-- just the name VURO please.) Attached is the old label for your reference, and the bottle type that will be used , which is a dark green Burgundy style bottle (pls ignore the label on the bottle). Please no grapes or wine glasses on the label. We are looking for something: eye catching / fun / ELEGANT (not cheap). We would be happy with a fun color too. Remember-- elegant, eye catching! Thanks!
Updates

Hi All, I think I made a mistake in my brief and have updated it. I also uploaded a competitor's label that we like very much to give better direction to what we are looking for. Also, the word Vuro cannot be vertical, nor can it be broken. It needs to read: VURO or Vuro. Thanks

Target Market(s)

American adults male and female.

Colors
abd036
33a6d7
33b8a4
ffcf3e

Requirements
Must have
• The mandatory information as shown on old labels. The word VURO should be very prominent.
Nice to have
• The uploaded photo of a competitor's prosecco shows a label we really like... if you could play around with this shape and style we'd be very happy.
Should not have
• No grape images, no wine glass images, no images of babies or children.

```html
<!DOCTYPE html>
<html lang="it">
<head>
<meta charset="utf-8">
<title>Vuro Prosecco – Label</title>
<link rel="stylesheet" href="https://fonts.googleapis.com/css2?family=Cormorant+Garamond:wght@700&family=Pinyon+Script&family=Montserrat:wght@500;600&display=swap">
<style>
  :root {
    --maroon: #7a0f3a;
    --rose: #d2456b;
    --blush: #e9a3a8;
    --pink: #c0305e;
    --paper: #ffffff;
    --backdrop: #f7f8fa;
  }
  html, body {
    margin: 0;
    padding: 0;
    width: 753px;
    height: 1200px;
    overflow: hidden;
    background: var(--backdrop);
  }
  .label {
    position: absolute;
    left: 36px;
    top: 165px;
    width: 680px;
    height: 870px;
    background: var(--paper);
    box-shadow: 0 2px 10px rgba(0,0,0,0.08);
    overflow: hidden;
  }
  .pattern {
    position: absolute;
    left: 0;
    top: 0;
    width: 100%;
    height: 356px;
    background:
      radial-gradient(circle at 45% 30%, var(--blush) 0%, transparent 40%),
      radial-gradient(circle at 80% 60%, var(--rose) 0%, transparent 45%),
      linear-gradient(135deg, var(--pink) 0%, var(--blush) 45%, var(--maroon) 100%);
  }
  .band {
    position: absolute;
    top: 356px;
    height: 12px;
    background: var(--maroon);
  }
  .band--left { left: 0; width: 190px; }
  .band--right { right: 0; width: 195px; }
  .name-block {
    position: absolute;
    left: 203px;
    top: 167px;
    width: 270px;
    height: 272px;
    background: var(--maroon);
    outline: 6px solid var(--paper);
    display: flex;
    align-items: center;
    justify-content: center;
  }
  .brand {
    margin: 0;
    font-family: "Montserrat", sans-serif;
    font-weight: 600;
    font-size: 64px;
    letter-spacing: 5px;
    color: var(--paper);
  }
  .wine {
    position: absolute;
    left: 0;
    width: 100%;
    text-align: center;
    color: var(--maroon);
    margin: 0;
  }
  .wine__type {
    top: 528px;
    font-family: "Cormorant Garamond", serif;
    font-weight: 700;
    font-size: 88px;
    line-height: 1;
    letter-spacing: 1px;
  }
  .wine__region {
    top: 660px;
    font-family: "Pinyon Script", cursive;
    font-size: 50px;
    line-height: 1;
  }
  .wine__designation {
    top: 718px;
    font-family: "Montserrat", sans-serif;
    font-weight: 600;
    font-size: 25px;
    letter-spacing: 1.5px;
  }
  .wine__style {
    top: 790px;
    font-family: "Montserrat", sans-serif;
    font-weight: 500;
    font-size: 17px;
  }
</style>
</head>
<body>
  <main class="label">
    <div class="pattern" role="img" aria-label="Decorative swirling petal pattern in pinks, blush and maroon"></div>
    <div class="band band--left"></div>
    <div class="band band--right"></div>
    <div class="name-block">
      <h1 class="brand">VURO</h1>
    </div>
    <p class="wine wine__type">PROSECCO</p>
    <p class="wine wine__region">Veneto</p>
    <p class="wine wine__designation">INDICAIONE GEOGRAFICA TIPICA</p>
    <p class="wine wine__style">FRIZZANTE</p>
  </main>
</body>
</html>
```